Australian Export Wine Label

Brand

To design a label based around Australia’s famous bush ranger Sam Ordway called Ordway’s Run.

Imagery for the label could be an abstract image of Sam’s armour of even of himself or we are open to other possibilities ranging from a traditional label to a more contemporary look and feel.

Images should not include guns and imagery used must be free of copyright.

Designs should be able to be printed by the standard 4 colour print process. As this is not an expensive product there will be no expensive label fiunishes such as gold foil or embossing

The range

The range of wines will consist of a 2011 Shiraz, 2012 Sauvignon Blanc and 2011 Chardonnay.

Market

The primary market for these wines is Ireland with the price range being in the $10-15 bracket. The wines will be available in independent retail shops and restaurants

Front Label Mandatories

1. Front Label: should not exceed 110mm x 80mm

2. Brand name - Ordway’s Run

3. Vintage & Variety – for example 2011 Shiraz

4. Origin – Wine of Australia

5. Text to appear on front label: Born in Co. Antrim, the remarkable Ruth Ordway had eight children including Australia’s most famous Bushranger Sam Ordway. The family’s wild and independent spirit is legendary in country Australia.

Back Label Mandatories

1. Back Label: 80mm x 80mm

2. Brand name

3. Vintage & Variety

4. Alcohol, Volume, Country of production

5. 13.0% VOL 750Ml (must be 4mm in height)

6. Contains egg, milk and nuts. Traces may remain

7. Please include the pregnant lady logo and a recycling logo

8. Wine of Australia

9. Space for barcode

10. Text to appear on back label (Shiraz):

Ordway’s Run is our vineyard named after the Ordway family, whose homestead stood here long before the vines were planted.
Our Ordway’s Run Shiraz is bold and full of flavour. Plums, cassis, chocolate and spice intermingle on the nose and palate, resulting in a full bodied, vibrant wine. Enjoy with a spirit of adventure and a hearty beef stew.

```html
<!DOCTYPE html>
<html lang="en">
<head>
<meta charset="utf-8">
<title>Ordway’s Run — 2011 Shiraz Label</title>
<link rel="stylesheet" href="https://fonts.googleapis.com/css2?family=Almendra:wght@400;700&family=Cinzel:wght@600&family=Open+Sans:ital,wght@1,400&display=swap">
<style>
  :root {
    --paper: #ffffff;
    --mauve: #98636a;
    --portrait-brown: #433630;
    --title-white: #ffffff;
    --ink: #111111;
    --rule: #6e4a50;
  }
  html, body {
    margin: 0;
    padding: 0;
    width: 1200px;
    height: 904px;
    overflow: hidden;
    background: var(--paper);
  }
  .canvas {
    position: relative;
    width: 1200px;
    height: 904px;
    background: var(--paper);
  }
  .label-frame {
    position: absolute;
    left: 82px;
    top: 93px;
    width: 1018px;
    height: 745px;
    background: var(--mauve);
  }
  .label-frame::before {
    content: "";
    position: absolute;
    inset: 6px;
    border: 4px solid var(--paper);
  }
  .label-field {
    position: absolute;
    inset: 13px;
    overflow: hidden;
  }
  .portrait {
    position: absolute;
    left: 26px;
    top: 100px;
    width: 412px;
    height: 640px;
  }
  .brand-name {
    position: absolute;
    left: 420px;
    top: 170px;
    width: 560px;
    margin: 0;
    text-align: center;
    white-space: nowrap;
    font-family: "Almendra", serif;
    font-weight: 400;
    font-size: 92px;
    line-height: 1;
    color: var(--title-white);
  }
  .vintage-row {
    position: absolute;
    left: 420px;
    top: 385px;
    width: 560px;
    display: flex;
    align-items: center;
    justify-content: center;
    gap: 8px;
  }
  .vintage-rule {
    width: 80px;
    height: 10px;
  }
  .vintage {
    margin: 0;
    font-family: "Cinzel", serif;
    font-weight: 600;
    font-size: 54px;
    line-height: 1;
    color: var(--ink);
    white-space: nowrap;
  }
  .story {
    position: absolute;
    left: 455px;
    top: 606px;
    width: 530px;
    margin: 0;
    font-family: "Open Sans", sans-serif;
    font-style: italic;
    font-size: 15.5px;
    line-height: 21px;
    color: var(--paper);
  }
  .story-line {
    display: block;
    white-space: nowrap;
  }
  .origin {
    position: absolute;
    right: 29px;
    top: 676px;
    margin: 0;
    font-family: "Open Sans", sans-serif;
    font-style: italic;
    font-size: 15.5px;
    line-height: 1;
    color: var(--paper);
  }
</style>
</head>
<body>
<div class="canvas">
  <div class="label-frame">
    <div class="label-field">
      <svg class="portrait" role="img" aria-label="Two-tone portrait of bushranger Sam Ordway with full beard" viewBox="0 0 412 640">
        <rect x="0" y="0" width="412" height="640" rx="150" ry="120" fill="var(--portrait-brown)"/>
      </svg>

      <h1 class="brand-name">Ordway’s Run</h1>

      <div class="vintage-row">
        <svg class="vintage-rule" viewBox="0 0 80 10" aria-hidden="true">
          <path d="M2 5 Q40 -1 78 5" fill="none" stroke="var(--rule)" stroke-width="1.5"/>
        </svg>
        <p class="vintage">2011 Shiraz</p>
        <svg class="vintage-rule" viewBox="0 0 80 10" aria-hidden="true">
          <path d="M2 5 Q40 -1 78 5" fill="none" stroke="var(--rule)" stroke-width="1.5"/>
        </svg>
      </div>

      <p class="story">
        <span class="story-line">Born in Co. Antrim, the remarkable Ruth Ordway had eight children including</span>
        <span class="story-line">Australia’s most famous Bushranger Sam Ordway. The family’s wild and</span>
        <span class="story-line">independent spirit is legendary in country Australia.</span>
      </p>
      <p class="origin">Made in Australia</p>
    </div>
  </div>
</div>
</body>
</html>
```